Letter Head / Envelopes
Business Card
Professional
Glen Hartwick Sr
Managing Partner
418 Tamsin Rd Alder Glen, ST 00471
glen@copperfieldre.com
www.copperfieldre.com

```html
<!DOCTYPE html>
<html lang="en">
<head>
<meta charset="utf-8">
<title>Copperfield Real Estate – Stationery</title>
<link href="https://fonts.googleapis.com/css2?family=Libre+Baskerville:wght@400;700&display=swap" rel="stylesheet">
<style>
  :root {
    --maroon: #8c2330;
    --maroon-dark: #731b27;
    --paper: #ffffff;
    --ink: #2a2a2a;
    --faint: #e6e3df;
    --backdrop: #ece7e0;
  }
  * { margin: 0; padding: 0; box-sizing: border-box; }
  html, body { width: 1200px; height: 744px; overflow: hidden; }
  body {
    position: relative;
    background: var(--backdrop);
    font-family: "Libre Baskerville", "Times New Roman", serif;
    color: var(--ink);
  }
  address { font-style: normal; }

  .brand { display: flex; align-items: center; gap: 8px; color: var(--maroon); font-weight: 700; line-height: 1.05; }
  .brand-square { background: var(--maroon); flex: none; }
  .brand-name { text-transform: uppercase; }

  .watermark {
    position: absolute; display: flex; flex-direction: column; align-items: center; justify-content: center;
    gap: 8px; color: var(--faint); font-weight: 700; text-transform: uppercase; text-align: center; line-height: 1.1;
  }
  .watermark .brand-square { background: var(--faint); }

  /* Letterhead */
  .letterhead {
    position: absolute; left: 29px; top: 29px; width: 523px; height: 679px;
    background: var(--paper); box-shadow: 0 2px 8px rgba(0,0,0,.18);
  }
  .letterhead::before { content: ""; position: absolute; left: 0; top: 0; bottom: 0; width: 12px; background: var(--maroon); }
  .letterhead .brand { position: absolute; left: 36px; top: 34px; font-size: 17px; }
  .letterhead .brand-square { width: 20px; height: 20px; }
  .letterhead .contact { position: absolute; left: 392px; top: 34px; font-size: 7.5px; line-height: 1.55; color: var(--maroon-dark); }
  .letterhead .watermark { left: 345px; top: 500px; width: 175px; height: 175px; font-size: 14px; }
  .letterhead .watermark .brand-square { width: 64px; height: 64px; }

  /* Business card */
  .business-card {
    position: absolute; left: 763px; top: 156px; width: 210px; height: 127px;
    background: var(--paper); box-shadow: 0 2px 6px rgba(0,0,0,.2);
  }
  .business-card::before { content: ""; position: absolute; left: 0; top: 0; bottom: 0; width: 6px; background: var(--maroon); }
  .business-card .brand { position: absolute; left: 16px; top: 42px; font-size: 8.5px; gap: 4px; }
  .business-card .brand-square { width: 10px; height: 10px; }
  .business-card .person { position: absolute; left: 112px; top: 16px; color: var(--maroon); }
  .business-card .person-name { font-size: 9px; font-weight: 700; }
  .business-card .person-title { font-size: 6px; margin-top: 2px; }
  .business-card .contact { position: absolute; left: 112px; top: 48px; font-size: 5.2px; line-height: 1.6; color: var(--maroon-dark); }

  /* Envelope */
  .envelope {
    position: absolute; left: 583px; top: 365px; width: 593px; height: 338px;
    background: var(--paper); box-shadow: 0 2px 8px rgba(0,0,0,.18);
  }
  .envelope .flap { position: absolute; left: 0; top: 0; width: 100%; height: 91px; }
  .envelope .bottom-rule { position: absolute; left: 0; right: 0; bottom: 0; height: 9px; background: var(--maroon); }
  .envelope .brand { position: absolute; left: 24px; top: 130px; font-size: 17px; }
  .envelope .brand-square { width: 20px; height: 20px; }
  .envelope .return-address { position: absolute; left: 24px; top: 176px; font-size: 8px; color: var(--maroon-dark); }
  .envelope .watermark { left: 430px; top: 170px; width: 145px; height: 155px; font-size: 12px; }
  .envelope .watermark .brand-square { width: 52px; height: 52px; }
</style>
</head>
<body>

  <section class="letterhead" aria-label="Letterhead">
    <div class="brand"><span class="brand-square"></span><span class="brand-name">Copperfield<br>Real Estate</span></div>
    <address class="contact">
      418 Tamsin Rd<br>
      Alder Glen, ST 00471<br>
      Phone: 555-201-0142<br>
      Fax: 555-201-0143<br>
      www.copperfieldre.com
    </address>
    <div class="watermark" role="img" aria-label="Faint brand mark decoration">
      <span class="brand-square"></span><span>Copperfield<br>Real Estate</span>
    </div>
  </section>

  <section class="business-card" aria-label="Business card">
    <div class="brand"><span class="brand-square"></span><span class="brand-name">Copperfield<br>Real Estate</span></div>
    <div class="person">
      <div class="person-name">Glen Hartwick Sr</div>
      <div class="person-title">Managing Partner</div>
    </div>
    <address class="contact">
      418 Tamsin Rd<br>
      Alder Glen, ST 00471<br>
      Phone: 555-201-0142<br>
      Fax: 555-201-0143<br>
      glen@copperfieldre.com<br>
      www.copperfieldre.com
    </address>
  </section>

  <section class="envelope" aria-label="Envelope">
    <svg class="flap" viewBox="0 0 593 91" preserveAspectRatio="none" aria-hidden="true">
      <path d="M0 91 L0 26 Q0 0 26 0 L567 0 Q593 0 593 26 L593 91 Z" fill="var(--maroon)"/>
    </svg>
    <div class="brand"><span class="brand-square"></span><span class="brand-name">Copperfield<br>Real Estate</span></div>
    <address class="return-address">418 Tamsin Rd, Alder Glen, ST 00471</address>
    <div class="watermark" role="img" aria-label="Faint brand mark decoration">
      <span class="brand-square"></span><span>Copperfield<br>Real Estate</span>
    </div>
    <div class="bottom-rule"></div>
  </section>

</body>
</html>
```